Marketing based tech company needs infographics

I need an infographic created about our process as it pertains to event organizers working with marketers, marketers working with event organizers and both working with sponsors.

3 sections
Event Organizers Steps: Total Timeline 3-10 days
1. Event organizer submits their deck (proposal)
2. It is sent to a vetter for review
3. The vetter provides edits
4. The event organizer approves the edits
5. The deck is turned into a website link
6. The deck is ready for the event organizer to send to sponsors
7. Sponsors open it and are wowed!
Marketer Steps: Total timeline 3-10 days
1. the marketer receives the deck
2. Provides feedback/edits to the event organizer
3. The event organizer approves the edits
6. The vetter is paid for their work immediately after the website goes live
Sponsors Steps: Total Timeline 30+ days
1. Sponsor is matched only with events that meet their demographics.
2. Event organizer submits their deck (proposal) to sponsor
3. The sponsor reviews the deck
4. If they are wowed they continue the conversation.
5. The event terms are negotiated.
6. The event organizer is paid 14 days prior to the event.
7. The event happens and is a success!

Target Market(s)

Minority-owned businesses and event planners.

Industry/Entity Type

Marketing

Font styles to use
Sans Serif

Colors
f78f20
0455a3
0692cd

Requirements
Must have
• 3 sections
• Event Organizers Steps: Total Timeline 3-10 days
• 1. Event organizer submits their deck (proposal)
• 2. It is sent to a vetter for review
• 3. The vetter provides edits
• 4. The event organizer approves the edits
• 5. The deck is turned into a website link
• 6. The deck is ready for the event organizer to send to sponsors
• 7. Sponsors open it and are wowed!
• Marketer Steps: Total timeline 3-10 days
• 1. the marketer receives the deck
• 2. Provides feedback/edits to the event organizer
• 3. The event organizer approves the edits
• 6. The vetter is paid for their work immediately after the website goes live
• Sponsors Steps: Total Timeline 30+ days
• 1. Sponsor is matched only with events that meet their demographics.
• 2. Event organizer submits their deck (proposal) to sponsor
• 3. The sponsor reviews the deck
• 4. If they are wowed they continue the conversation.
• 5. The event terms are negotiated.
• 6. The event organizer is paid 14 days prior to the event.
• 7. The event happens and is a success!
Nice to have
• To incorporate the styles of the graphics and icons attached
Should not have
• Be creative!

```html
<!DOCTYPE html>
<html lang="en">
<head>
<meta charset="utf-8">
<title>Our Processes as Event Organizers</title>
<link href="https://fonts.googleapis.com/css2?family=Oswald:wght@300&family=Exo+2:wght@800&family=Fira+Sans:wght@300;400&display=swap" rel="stylesheet">
<style>
  :root{
    --orange:#f78f20;
    --navy:#0c2a5b;
    --blue:#0455a3;
    --sky:#0692cd;
    --ink:#2b2b2b;
    --rule:#8a8f99;
    --white:#ffffff;
  }
  *{box-sizing:border-box;margin:0;padding:0}
  html,body{width:830px;height:1200px;overflow:hidden}
  body{background:var(--orange);font-family:"Fira Sans",sans-serif;color:var(--ink)}
  .sheet{position:absolute;left:17px;top:17px;width:796px;height:1166px;background:var(--white)}
  .canvas{position:absolute;left:0;top:0;width:830px;height:1200px}

  .brand{position:absolute;top:100px;left:0;width:830px;text-align:center;
    font-family:"Fira Sans",sans-serif;font-weight:300;font-size:27px;color:var(--orange);letter-spacing:.3px}
  .brand-dot{position:absolute;left:401px;top:50px;width:28px;height:28px;border-radius:50%;background:var(--orange)}

  .title{position:absolute;top:162px;left:0;width:830px;text-align:center;
    font-family:"Oswald",sans-serif;font-weight:300;font-size:39px;color:var(--navy);letter-spacing:-.2px}

  .divider{position:absolute;top:245px;width:1px;height:906px;background:var(--rule)}

  .column{position:absolute;top:0;height:1200px}
  .col-organizers{left:0;width:286px}
  .col-marketers{left:286px;width:255px}
  .col-sponsors{left:541px;width:289px}

  .col-heading{position:absolute;top:256px;width:100%;height:72px;display:flex;align-items:center;justify-content:center;text-align:center;
    font-family:"Exo 2",sans-serif;font-weight:800;font-size:20px;line-height:24px;color:var(--navy);text-transform:uppercase}
  .col-organizers .col-heading{left:0;width:312px}
  .timeline{position:absolute;top:338px;height:52px;border-top:1px solid var(--navy);border-bottom:1px solid var(--navy);
    display:flex;align-items:center;justify-content:center;text-align:center;font-size:14.5px;line-height:21px;color:var(--ink)}
  .col-organizers .timeline{left:69px;width:174px}
  .col-marketers .timeline{left:39px;width:174px}
  .col-sponsors .timeline{left:33px;width:174px}

  .track{position:absolute;width:0;border-left:1.5px dashed var(--orange)}

  .badge{position:absolute;width:48px;height:48px;border-radius:50%;background:var(--white);
    border:3px solid #e9edf3;border-left-color:var(--orange);border-top-color:var(--orange);transform:rotate(-20deg);
    box-shadow:0 2px 5px rgba(0,0,0,.18)}
  .badge-inner{position:absolute;inset:0;transform:rotate(20deg);display:flex;align-items:center;justify-content:center;gap:2px}
  .badge-num{font-family:"Fira Sans",sans-serif;font-weight:300;font-size:27px;line-height:1;color:var(--blue);margin-left:-3px}
  .badge-icon{width:12px;height:15px;border:1.5px solid var(--navy);border-radius:1px;position:relative}
  .badge-icon::before,.badge-icon::after{content:"";position:absolute;left:2px;right:2px;height:1.2px;background:var(--navy)}
  .badge-icon::before{top:3px}
  .badge-icon::after{top:7px}

  .step-text{position:absolute;font-size:14.5px;line-height:20.8px;color:var(--ink);font-weight:300}
  .col-organizers .badge{left:77px}
  .col-organizers .step-text{left:144px;width:140px}
  .col-marketers .badge{left:38px}
  .col-marketers .step-text{left:101px;width:135px}
  .col-sponsors .badge{left:41px}
  .col-sponsors .step-text{left:105px;width:135px}
</style>
</head>
<body>
<div class="canvas">
  <div class="sheet"></div>

  <span class="brand-dot"></span>
  <div class="brand">PitchProof</div>
  <h1 class="title">OUR PROCESSES AS EVENT ORGANIZERS</h1>

  <div class="divider" style="left:286px"></div>
  <div class="divider" style="left:541px"></div>

  <!-- Event organizers -->
  <section class="column col-organizers">
    <h2 class="col-heading">Event<br>Organizers<br>Steps</h2>
    <p class="timeline">Total Timeline:<br>3-10 days</p>
    <div class="track" style="left:100px;top:462px;height:610px"></div>

    <div class="badge" style="top:414px"><div class="badge-inner"><span class="badge-num">1</span><span class="badge-icon"></span></div></div>
    <p class="step-text" style="top:411px">Event organizer submits their deck (proposal)</p>
    <div class="badge" style="top:518px"><div class="badge-inner"><span class="badge-num">2</span><span class="badge-icon"></span></div></div>
    <p class="step-text" style="top:514px">It is sent to a vetter for review</p>
    <div class="badge" style="top:618px"><div class="badge-inner"><span class="badge-num">3</span><span class="badge-icon"></span></div></div>
    <p class="step-text" style="top:617px">The vetter provides edits</p>
    <div class="badge" style="top:702px"><div class="badge-inner"><span class="badge-num">4</span><span class="badge-icon"></span></div></div>
    <p class="step-text" style="top:698px">The event organizer approves the edits</p>
    <div class="badge" style="top:824px"><div class="badge-inner"><span class="badge-num">5</span><span class="badge-icon"></span></div></div>
    <p class="step-text" style="top:822px">The deck is turned into a website link</p>
    <div class="badge" style="top:928px"><div class="badge-inner"><span class="badge-num">6</span><span class="badge-icon"></span></div></div>
    <p class="step-text" style="top:925px">The deck is ready for the event organizer to send to sponsors</p>
    <div class="badge" style="top:1072px"><div class="badge-inner"><span class="badge-num">7</span><span class="badge-icon"></span></div></div>
    <p class="step-text" style="top:1069px">Sponsors open it and are wowed!</p>
  </section>

  <!-- Marketers -->
  <section class="column col-marketers">
    <h2 class="col-heading">Marketer<br>Steps</h2>
    <p class="timeline">Total Timeline:<br>3-10 days</p>
    <div class="track" style="left:61px;top:462px;height:610px"></div>

    <div class="badge" style="top:414px"><div class="badge-inner"><span class="badge-num">1</span><span class="badge-icon"></span></div></div>
    <p class="step-text" style="top:411px">The marketer receives the deck</p>
    <div class="badge" style="top:488px"><div class="badge-inner"><span class="badge-num">2</span><span class="badge-icon"></span></div></div>
    <p class="step-text" style="top:487px">Provides feedback/edits to the event organizer</p>
    <div class="badge" style="top:608px"><div class="badge-inner"><span class="badge-num">3</span><span class="badge-icon"></span></div></div>
    <p class="step-text" style="top:604px">The event organizer approves the edits</p>
    <div class="badge" style="top:724px"><div class="badge-inner"><span class="badge-num">4</span><span class="badge-icon"></span></div></div>
    <p class="step-text" style="top:722px">The deck is turned into a website link</p>
    <div class="badge" style="top:826px"><div class="badge-inner"><span class="badge-num">5</span><span class="badge-icon"></span></div></div>
    <p class="step-text" style="top:818px">The vetter is paid for their work immediately after the website goes live</p>
    <div class="badge" style="top:960px"><div class="badge-inner"><span class="badge-num">6</span><span class="badge-icon"></span></div></div>
    <p class="step-text" style="top:958px">The deck is ready for the event organizer to send to sponsors</p>
    <div class="badge" style="top:1072px"><div class="badge-inner"><span class="badge-num">7</span><span class="badge-icon"></span></div></div>
    <p class="step-text" style="top:1074px">Sponsors open it and are wowed!</p>
  </section>

  <!-- Sponsors -->
  <section class="column col-sponsors">
    <h2 class="col-heading">Sponsors<br>Steps</h2>
    <p class="timeline">Total Timeline:<br>30+ days</p>
    <div class="track" style="left:64px;top:462px;height:600px"></div>

    <div class="badge" style="top:414px"><div class="badge-inner"><span class="badge-num">1</span><span class="badge-icon"></span></div></div>
    <p class="step-text" style="top:411px">Sponsor is matched only with events that meet their demographics.</p>
    <div class="badge" style="top:554px"><div class="badge-inner"><span class="badge-num">2</span><span class="badge-icon"></span></div></div>
    <p class="step-text" style="top:550px">Event organizer submits their deck (proposal) to sponsor</p>
    <div class="badge" style="top:669px"><div class="badge-inner"><span class="badge-num">3</span><span class="badge-icon"></span></div></div>
    <p class="step-text" style="top:669px">The sponsor reviews the deck</p>
    <div class="badge" style="top:749px"><div class="badge-inner"><span class="badge-num">4</span><span class="badge-icon"></span></div></div>
    <p class="step-text" style="top:746px">If they are wowed they continue the conversation.</p>
    <div class="badge" style="top:864px"><div class="badge-inner"><span class="badge-num">5</span><span class="badge-icon"></span></div></div>
    <p class="step-text" style="top:865px">The event terms are negotiated.</p>
    <div class="badge" style="top:947px"><div class="badge-inner"><span class="badge-num">6</span><span class="badge-icon"></span></div></div>
    <p class="step-text" style="top:942px">The event organizer is paid 14 days prior to the event.</p>
    <div class="badge" style="top:1062px"><div class="badge-inner"><span class="badge-num">7</span><span class="badge-icon"></span></div></div>
    <p class="step-text" style="top:1060px">The event happens and is a success!</p>
  </section>
</div>
</body>
</html>
```